Design for the A4 Letterhead, envelope and A4 Folder

Design have to be clean, professional, unique (eye catchy) and high end.
Colors: Yellow (Code: 803C), Darker Grey and Black or white (optional)
Logo can be in white or black

Letterhead:
Contain: 1. Corvalis Logo
2. Slogan "MADE WITH PRIDE"
3. Company information:
Corvalis Valves Pte. Ltd. (Singapore)
Registration no: 201764219K
Tel: (65) 6182 4906
Fax: (65) 6247 9158
Email: sales@corvalisvalves.example
Website: http://www.corvalisvalves.example
4. Logo watermark

Envelope:
Contain: 1. Corvalis Logo
3. website: http://www.corvalisvalves.example and email address:
sales@corvalisvalves.example
4. Logo watermark

Folder:
Contain: 1. Corvalis Logo
3. Company's information:
Tel: (65) 6182 4906
Fax: (65) 6247 9158
4. QR Code
5. Logo watermark
6. On the inside there is a space to insert business card. Contrast colors
between the inside and cover.

For the Folder design, please be informed that we would prefer to have the Corvalis logo on the left hand side of the cover page, rather than on the right hand side.And also if we could highlight the "Made with Pride" slogan with either the yellow box or black/grey box depending on the background color.For the Envelope design,it does not matter where the position of the logo is. But please also highlight the "Made with Pride" Slogan For the Letterhead design, the position of the logo must be on the left hand side and the slogan must be highlighted. In addition, please include the following company information (only for the letterhead design)Corvalis Valves Pte. Ltd. (Singapore)Registration no: 201764219KTel: (65) 6182 4906Fax: (65) 6247 9158Email: sales@corvalisvalves.exampleWebsite: http://www.corvalisvalves.example Added Wednesday, August 2, 2017

Target Market(s)

Business to Business, High End market

Industry/Entity Type

It Professional

Font styles to use
Serif

Requirements
Must have
• Design have to be clean, professional, unique (eye catchy) and high end.
Nice to have
• color contrast but still maintaining the professionalism and the seriousness
Should not have
• Messy look, futuristic look, too crowded

```html
<!DOCTYPE html>
<html lang="en">
<head>
<meta charset="utf-8">
<title>Corvalis Valves – A4 Letterhead</title>
<link rel="stylesheet" href="https://fonts.googleapis.com/css2?family=Oswald:wght@500;600&family=Open+Sans:wght@400;700&display=swap">
<style>
  :root {
    --brand-yellow: #f5e829;
    --brand-yellow-soft: #f7f3c4;
    --brand-dark: #3a3a3c;
    --brand-black: #111111;
    --paper: #ffffff;
    --backdrop: #e6da7c;
    --text: #1a1a1a;
    --text-muted: #4a4a4a;
  }
  * { margin: 0; padding: 0; box-sizing: border-box; }
  html, body {
    width: 1200px;
    height: 784px;
    overflow: hidden;
    background: var(--backdrop);
  }
  .canvas {
    width: 1200px;
    height: 784px;
    display: flex;
    align-items: center;
    justify-content: center;
  }
  .letterhead {
    position: relative;
    width: 524px;
    height: 742px;
    background: var(--paper);
    box-shadow: 0 6px 18px rgba(90, 80, 20, 0.25);
    overflow: hidden;
  }

  /* Header */
  .header-accent {
    position: absolute;
    left: 0;
    top: 0;
    width: 7px;
    height: 46px;
    background: linear-gradient(90deg, var(--brand-black), var(--brand-dark));
  }
  .brand {
    position: absolute;
    left: 28px;
    top: 18px;
    display: flex;
    align-items: center;
    gap: 8px;
  }
  .brand-mark {
    width: 22px;
    height: 22px;
    border-radius: 50%;
    background: var(--brand-black);
  }
  .brand-name {
    font-family: "Oswald", sans-serif;
    font-weight: 600;
    font-size: 22px;
    letter-spacing: 1px;
    color: var(--brand-black);
    text-transform: uppercase;
  }
  .header-rule {
    position: absolute;
    left: 150px;
    right: 0;
    top: 52px;
    height: 4px;
    background: var(--brand-yellow);
  }

  /* Watermark */
  .watermark {
    position: absolute;
    left: 150px;
    top: 458px;
    width: 168px;
    height: 168px;
  }

  /* Footer */
  .footer-slogan {
    position: absolute;
    right: 168px;
    bottom: 66px;
    font-family: "Oswald", sans-serif;
    font-weight: 500;
    font-size: 24px;
    letter-spacing: 0.5px;
    color: var(--brand-yellow);
    text-transform: uppercase;
    line-height: 1;
  }
  .footer-company {
    position: absolute;
    right: 168px;
    bottom: 46px;
    font-family: "Open Sans", sans-serif;
    font-weight: 700;
    font-size: 10.5px;
    color: var(--text);
  }
  .footer-contacts {
    position: absolute;
    left: 18px;
    right: 18px;
    bottom: 18px;
    display: flex;
    justify-content: space-between;
    font-family: "Open Sans", sans-serif;
    font-size: 7px;
    line-height: 1.2;
    color: var(--text-muted);
    white-space: nowrap;
  }
  .contact-item {
    display: flex;
    align-items: center;
    gap: 3px;
  }
  .contact-icon {
    width: 7px;
    height: 7px;
    flex: none;
  }
  .footer-band {
    position: absolute;
    left: 0;
    right: 0;
    bottom: 0;
    height: 7px;
    display: flex;
  }
  .footer-band-yellow { flex: 0 0 68%; background: var(--brand-yellow); }
  .footer-band-dark { flex: 1; background: linear-gradient(90deg, var(--brand-dark), var(--brand-black)); }
</style>
</head>
<body>
<main class="canvas">
  <article class="letterhead">
    <header>
      <div class="header-accent"></div>
      <div class="brand">
        <span class="brand-mark"></span>
        <span class="brand-name">Corvalis</span>
      </div>
      <div class="header-rule"></div>
    </header>

    <svg class="watermark" viewBox="0 0 168 168" aria-hidden="true">
      <circle cx="84" cy="84" r="76" fill="none" stroke="var(--brand-yellow-soft)" stroke-width="12"/>
    </svg>

    <footer>
      <p class="footer-slogan">Made with Pride</p>
      <p class="footer-company">Corvalis Valves Pte. Ltd. (Singapore)</p>
      <div class="footer-contacts">
        <span class="contact-item">
          <svg class="contact-icon" viewBox="0 0 10 10"><circle cx="5" cy="5" r="5" fill="var(--brand-dark)"/><path d="M3.3 2.6l1 1-.6.7a3.5 3.5 0 0 0 2 2l.7-.6 1 1-.7.8C4.9 7.4 2.6 5.1 2.5 3.3z" fill="#fff"/></svg>
          (65) 6182 4906
        </span>
        <span class="contact-item">
          <svg class="contact-icon" viewBox="0 0 10 10"><circle cx="5" cy="5" r="5" fill="var(--brand-dark)"/><rect x="2.8" y="3.4" width="4.4" height="3.4" fill="#fff"/></svg>
          (65) 6247 9158
        </span>
        <span class="contact-item">
          <svg class="contact-icon" viewBox="0 0 10 10"><circle cx="5" cy="5" r="5" fill="var(--brand-dark)"/><path d="M2.6 3.3h4.8v3.4H2.6z M2.6 3.3L5 5.2l2.4-1.9" fill="none" stroke="#fff" stroke-width=".8"/></svg>
          sales@corvalisvalves.example
        </span>
        <span class="contact-item">
          <svg class="contact-icon" viewBox="0 0 10 10"><circle cx="5" cy="5" r="5" fill="var(--brand-dark)"/><circle cx="5" cy="5" r="2.5" fill="none" stroke="#fff" stroke-width=".8"/></svg>
          www.corvalisvalves.example
        </span>
        <span class="contact-item">
          <svg class="contact-icon" viewBox="0 0 10 10"><circle cx="5" cy="5" r="5" fill="var(--brand-dark)"/></svg>
          Regd. No.: 201764219K
        </span>
      </div>
      <div class="footer-band">
        <span class="footer-band-yellow"></span>
        <span class="footer-band-dark"></span>
      </div>
    </footer>
  </article>
</main>
</body>
</html>
```